Korimet Business Cards

Korimet is a software startup and we are looking for business cards that help convey our employee personalities, as well as the professionalism of the company.
Our company font is Comfortaa - and the company logo is attached (we are okay having the text beside the logo if applicable) where we can find the company colour scheme. Cards can be horizontal or vertical format.
We are looking for a two sided business card - on the front we will see the personal details of the employee (name, position, email and phone number), and then on the back, we will see the business details (name and logo, address, phone number, website, email, company tagline: "Accelerating technology disruption in the automotive market")
We want the design to be clean and simple, but also fun, modern, and capturing of a young startup vibe.

```html
<!DOCTYPE html>
<html lang="en">
<head>
<meta charset="utf-8">
<title>Korimet Business Cards</title>
<link rel="stylesheet" href="https://fonts.googleapis.com/css2?family=Comfortaa:wght@700&family=Montserrat:ital,wght@0,400;0,700;1,400&display=swap">
<style>
  :root {
    --bg: #ececef;
    --card: #ffffff;
    --indigo: #4b47a0;
    --indigo-light: #6659a8;
    --magenta: #b04f9c;
    --ink: #222228;
  }
  * { box-sizing: border-box; margin: 0; padding: 0; }
  html, body { width: 1200px; height: 1059px; overflow: hidden; background: var(--bg); }
  body { position: relative; font-family: "Montserrat", sans-serif; }

  .card {
    position: absolute;
    left: 256px;
    width: 688px;
    height: 392px;
    background: var(--card);
    border-radius: 22px;
    overflow: hidden;
    box-shadow: 0 8px 20px rgba(0,0,0,.18);
  }
  .card--front { top: 89px; }
  .card--back { top: 548px; }

  .wave { position: absolute; inset: 0; width: 100%; height: 100%; }

  .brand {
    position: absolute;
    display: flex;
    flex-direction: column;
    align-items: center;
    gap: 14px;
  }
  .brand__dot { width: 84px; height: 84px; border-radius: 50%; background: var(--indigo); }
  .brand__name {
    font-family: "Comfortaa", sans-serif;
    font-weight: 700;
    color: var(--indigo);
    font-size: 46px;
    letter-spacing: 1px;
    line-height: 1;
  }
  .card--front .brand { left: 28px; top: 48px; width: 190px; }
  .card--back .brand { left: 0; right: 0; top: 62px; }
  .card--back .brand__dot { width: 100px; height: 100px; }
  .card--back .brand__name { font-size: 56px; }

  .person {
    position: absolute;
    right: 34px;
    top: 232px;
    text-align: right;
    color: #fff;
  }
  .person__name { font-weight: 700; font-size: 28px; letter-spacing: 1px; text-transform: uppercase; line-height: 1; }
  .person__role { font-size: 16px; margin-top: 8px; letter-spacing: .3px; }
  .person__contact { margin-top: 22px; font-size: 18px; line-height: 26px; }
  .person__contact li { list-style: none; display: flex; justify-content: flex-end; align-items: center; gap: 8px; }

  .icon { width: 15px; height: 15px; flex: none; }
  .icon--white { fill: #fff; }
  .icon--accent { fill: var(--magenta); }

  .company-info {
    position: absolute;
    left: 0; right: 0;
    top: 288px;
    color: var(--ink);
    font-size: 16px;
    letter-spacing: .3px;
  }
  .company-info p { display: flex; justify-content: center; align-items: center; gap: 6px; line-height: 30px; }
  .company-info .sep { width: 8px; }

  .tagline {
    position: absolute;
    left: 0; right: 0; bottom: 0;
    height: 38px;
    background: linear-gradient(90deg, var(--indigo-light), var(--indigo));
    color: #fff;
    font-style: italic;
    font-size: 17px;
    letter-spacing: .3px;
    display: flex;
    align-items: center;
    justify-content: center;
  }
</style>
</head>
<body>

<section class="card card--front">
  <svg class="wave" viewBox="0 0 688 392" aria-hidden="true">
    <defs>
      <linearGradient id="band" x1="0" x2="1" y1="0" y2="0">
        <stop offset="0" stop-color="#5f5aa5"/>
        <stop offset="1" stop-color="#b04f9c"/>
      </linearGradient>
      <linearGradient id="field" x1="0" x2="1" y1="0" y2="0">
        <stop offset="0" stop-color="#6659a8"/>
        <stop offset="1" stop-color="#4b47a0"/>
      </linearGradient>
    </defs>
    <path d="M43,281 C90,303 140,305 180,298 C300,275 430,108 547,108 C600,108 640,130 663,158 C630,135 590,120 547,120 C420,120 300,292 180,306 C130,311 80,300 43,281 Z" fill="url(#band)"/>
    <path d="M0,240 C40,292 80,315 125,315 C260,315 420,128 547,128 C612,128 660,160 688,186 L688,392 L0,392 Z" fill="url(#field)"/>
  </svg>

  <div class="brand">
    <span class="brand__dot"></span>
    <span class="brand__name">korimet</span>
  </div>

  <div class="person">
    <h1 class="person__name">Jonah Reeve</h1>
    <p class="person__role">CEO/Founder</p>
    <ul class="person__contact">
      <li>+123.555.0142
        <svg class="icon icon--white" viewBox="0 0 24 24"><path d="M6.6 10.8a15.1 15.1 0 0 0 6.6 6.6l2.2-2.2a1 1 0 0 1 1-.25 11.4 11.4 0 0 0 3.6.57 1 1 0 0 1 1 1V20a1 1 0 0 1-1 1A17 17 0 0 1 3 4a1 1 0 0 1 1-1h3.5a1 1 0 0 1 1 1c0 1.25.2 2.45.57 3.6a1 1 0 0 1-.25 1z"/></svg>
      </li>
      <li>jonah@korimet.com.au
        <svg class="icon icon--white" viewBox="0 0 24 24"><path d="M2 5h20v2l-10 6L2 7z M2 9l10 6 10-6v10H2z"/></svg>
      </li>
    </ul>
  </div>
</section>

<section class="card card--back">
  <div class="brand">
    <span class="brand__dot"></span>
    <span class="brand__name">korimet</span>
  </div>

  <div class="company-info">
    <p>
      <svg class="icon icon--accent" viewBox="0 0 24 24"><path d="M12 2a7 7 0 0 0-7 7c0 5 7 13 7 13s7-8 7-13a7 7 0 0 0-7-7zm0 9.5A2.5 2.5 0 1 1 12 6.5a2.5 2.5 0 0 1 0 5z"/></svg>
      Linden, Harrowgate Vale Park, 1620
    </p>
    <p>
      <svg class="icon icon--accent" viewBox="0 0 24 24"><path d="M6.6 10.8a15.1 15.1 0 0 0 6.6 6.6l2.2-2.2a1 1 0 0 1 1-.25 11.4 11.4 0 0 0 3.6.57 1 1 0 0 1 1 1V20a1 1 0 0 1-1 1A17 17 0 0 1 3 4a1 1 0 0 1 1-1h3.5a1 1 0 0 1 1 1c0 1.25.2 2.45.57 3.6a1 1 0 0 1-.25 1z"/></svg>
      +987.555.0198<span class="sep"></span>
      <svg class="icon icon--accent" viewBox="0 0 24 24"><path d="M2 5h20v2l-10 6L2 7z M2 9l10 6 10-6v10H2z"/></svg>
      service@korimet.com.au<span class="sep"></span>
      <svg class="icon icon--accent" viewBox="0 0 24 24"><path d="M12 2a10 10 0 1 0 0 20 10 10 0 0 0 0-20zm0 2c1 1.3 1.8 3 2.1 5H9.9C10.2 7 11 5.3 12 4zm-2.1 7h4.2c0 2.2-.8 4.4-2.1 6-1.3-1.6-2.1-3.8-2.1-6zm-5.8 0h3.8c.1 2 .7 3.9 1.6 5.5A8 8 0 0 1 4.1 11zm12 0h3.8a8 8 0 0 1-5.4 5.5c.9-1.6 1.5-3.5 1.6-5.5zM4.1 9a8 8 0 0 1 5.4-4.5C8.6 6 8.1 7.5 7.9 9zm12 0c-.2-1.5-.7-3-1.6-4.5A8 8 0 0 1 19.9 9z"/></svg>
      www.korimet.com.au
    </p>
  </div>

  <p class="tagline">“Accelerating technology disruption in the automotive market”</p>
</section>

</body>
</html>
```